・昆布のパッケージシールラベルのデザインの作成をお願いします。 【 依頼内容 】 ・サイズ:○ 縦:150㎜○ 横:100㎜ ・作成数: 1種類 ・利用用途:商品ラベルシール(表のみ) 【 デザインイメージ 】 ・ターゲット層:お料理される方。年配女性。健康に気を使う方。 ・雰囲気:シンプルかつ高級感があるパッケージを希望しています。 ・他商品と差別化する上でターゲットを意識した背景イメージやイラスト入り可能ならお願いします。 【 他社参考URL】 下記参考URL参照下さい。 【 商品名等 】 ・商品名:磯香寿昆布(漢字かなレイアウトおまかせします。) ・入れてほしい文言:①上記商品名②ブランド名:ORVANE(サイズ控えめで)。べつでJPEGにロゴデザイン入れてます。こちらあまり強調したくないので英文字のみだけ控えめで記載でも構いません。③歯舞産④おだし・昆布水用に ・参考デザイン: 別途JPEG参照下さい。。弊社ロゴもあります。 【 納品 】 ・印刷会社様にお願いできるフォーマットでお願いします。当方知識少ないですがai、psdデータ、他jpeg/pngデータも同時に。この辺の経験ある方だと助かります。 納品物の著作権は弊社に譲渡いただき、著作者人格権を行使しないことにご同意の上ご応募ください。 【 禁止事項 】 ・他で登録されているデザインの転用 ・他のクライアントへ提出した内容の転用 【 契約金額(税抜) 】 1万5千円 ※契約金額(税込)からシステム利用料を差し引いた金額が、ワーカーさまの受取金額となります その他ご質問等ありましたら、お気軽にお問い合わせください。 ご応募をお待ちしております! その他ご質問等ありましたら、気軽にお問い合わせください。 ご応募をお待ちしております! |
| https://www.torivamart.example/s?k=%E6%A0%B9%E6%98%86%E5%B8%83 https://find.pelnoshop.example/search/mall/%E6%98%86%E5%B8%83/ | ||

```html
<!DOCTYPE html>
<html lang="ja">
<head>
<meta charset="utf-8">
<title>磯香寿昆布 ラベル</title>
<link rel="stylesheet" href="https://fonts.googleapis.com/css2?family=Shippori+Mincho+B1:wght@700;800&family=Noto+Serif+JP:wght@700&display=swap">
<style>
  :root {
    --backdrop: #f1f1f1;
    --paper: #ffffff;
    --paper-edge: #dedede;
    --kelp: #24433a;
    --ice: #8cc3d6;
    --ink: #111111;
    --seal: #c8201e;
    --title-ink: #ffffff;
  }
  html, body {
    margin: 0;
    padding: 0;
    width: 1200px;
    height: 1200px;
    overflow: hidden;
    background: var(--backdrop);
  }
  .label {
    position: absolute;
    left: 320px;
    top: 173px;
    width: 560px;
    height: 840px;
    background: var(--paper);
    box-shadow: 0 0 0 1px var(--paper-edge);
  }
  .label-art {
    position: absolute;
    left: 88px;
    top: 66px;
    width: 358px;
    height: 684px;
    border-radius: 24px;
    background: linear-gradient(180deg, var(--ice) 0%, var(--kelp) 16%, var(--kelp) 100%);
  }
  .vertical {
    position: absolute;
    writing-mode: vertical-rl;
    text-orientation: upright;
    margin: 0;
    font-family: "Noto Serif JP", serif;
    font-weight: 700;
    color: var(--ink);
    white-space: nowrap;
  }
  .origin {
    left: 462px;
    top: 72px;
    font-size: 30px;
    letter-spacing: 6px;
  }
  .usage {
    left: 26px;
    top: 372px;
    font-size: 32px;
    letter-spacing: 14px;
  }
  .product-name {
    left: 234px;
    top: 190px;
    font-family: "Shippori Mincho B1", serif;
    font-weight: 800;
    font-size: 66px;
    letter-spacing: 22px;
    color: var(--title-ink);
  }
  .brand {
    position: absolute;
    margin: 0;
    right: 114px;
    top: 772px;
    font-family: "Noto Serif JP", serif;
    font-weight: 700;
    font-size: 17px;
    letter-spacing: 3px;
    color: var(--seal);
  }
</style>
</head>
<body>
  <main class="label">
    <div class="label-art" role="img" aria-label="雪をいただく山の頂と、波打つ昆布のイラスト"></div>
    <p class="vertical origin">北海道　歯舞産</p>
    <h1 class="vertical product-name">磯香寿昆布</h1>
    <p class="vertical usage">おだし・昆布水用に</p>
    <p class="brand">ORVANE</p>
  </main>
</body>
</html>
```